Magician | Speaker looks for an innovative business card design

I'm a magician and public speaker offering artistic and modern magical experiences.
I'm based in Brussels (Belgium.) I love magic performed up-close, creating a space of intimacy, even when I'm on stage.
The final design should communicate professionalism, elegance, artistry, and a friendly kind personality

I would like to see designs based either on my photos and/or the way I sign my name Theo Varn (see attached files for more info.)
Additional photos and more info about what I offer can be seen at www.theo-varn.net

My current business card design is also attached. I like the fact that the reverse of my current design includes quotes from master magicians about magic, changing the way my participants see the art of magic.

Note: I would like a double-sided card design. However, I need white space on the reverse to be able to write things on for my performances.

Details to include on the card:
Artist name: Theo Varn
Offer: magician + (public) speaker or magic + (public) speaking (the + sign can be replaced by another character, like a bullet or a pipe)
Phone: +32 471 236 519
Email: book@theo-varn.net
(optional) Website: www.theo-varn.net or theo-varn.net

Target Market(s)

Corporate, organisations, companies as well as individuals

Industry/Entity Type

Artists

Colors

Designer to choose colors to be used in the design.

Requirements
Nice to have
• A side with a mirror could be nice

```html
<!DOCTYPE html>
<html lang="en">
<head>
<meta charset="utf-8">
<title>Theo Varn — Business Card</title>
<link rel="stylesheet" href="https://fonts.googleapis.com/css2?family=Almendra+SC&family=Josefin+Sans:wght@300;400&display=swap">
<style>
  :root {
    --page: #ececec;
    --card: #050505;
    --ink: #f2f2f2;
    --ink-soft: #cfcfcf;
    --rule: #bdbdbd;
    --photo-dark: #0a0a0a;
    --photo-mid: #2a2522;
    --photo-skin: #8a6a5c;
  }
  * { box-sizing: border-box; margin: 0; padding: 0; }
  html, body {
    width: 1200px;
    height: 800px;
    overflow: hidden;
    background: var(--page);
  }
  .business-card {
    position: absolute;
    left: 150px;
    top: 155px;
    width: 900px;
    height: 490px;
    background: var(--card);
    box-shadow: 0 10px 30px rgba(0,0,0,0.25);
    overflow: hidden;
  }
  .rotated {
    position: absolute;
    white-space: nowrap;
    transform: translate(-50%, -50%) rotate(-90deg);
  }
  .tagline {
    left: 52px;
    top: 250px;
    font-family: "Josefin Sans", sans-serif;
    font-weight: 300;
    font-size: 20px;
    letter-spacing: 2px;
    color: var(--ink-soft);
  }
  .performer-photo {
    position: absolute;
    left: 116px;
    top: 55px;
    width: 350px;
    height: 370px;
    background:
      radial-gradient(ellipse at 45% 30%, var(--photo-skin) 0%, rgba(138,106,92,0.35) 18%, transparent 40%),
      radial-gradient(ellipse at 55% 65%, rgba(160,110,110,0.55) 0%, transparent 35%),
      linear-gradient(180deg, var(--photo-mid) 0%, var(--photo-dark) 100%);
  }
  .artist-name {
    left: 576px;
    top: 245px;
    font-family: "Almendra SC", serif;
    font-size: 64px;
    letter-spacing: 3px;
    color: var(--ink);
  }
  .rule {
    position: absolute;
    top: 55px;
    width: 2px;
    height: 345px;
    background: var(--rule);
  }
  .rule--inner { left: 690px; }
  .rule--outer { left: 764px; }
  .specialty {
    left: 727px;
    top: 228px;
    font-family: "Josefin Sans", sans-serif;
    font-weight: 400;
    font-size: 21px;
    letter-spacing: 2px;
    color: var(--ink);
    display: flex;
    align-items: center;
    gap: 10px;
  }
  .specialty .dot {
    width: 12px;
    height: 12px;
    border-radius: 50%;
    background: var(--ink);
  }
</style>
</head>
<body>
  <div class="business-card">
    <p class="rotated tagline">NOW YOU SEE ME...</p>
    <div class="performer-photo" role="img" aria-label="Photo of a magician's hands spreading playing cards against a dark background"></div>
    <h1 class="rotated artist-name">Theo Varn</h1>
    <span class="rule rule--inner"></span>
    <span class="rule rule--outer"></span>
    <p class="rotated specialty">MAGICIAN <span class="dot"></span> PUBLIC SPEAKER</p>
  </div>
</body>
</html>
```